Brochure Design Project for Building Designer

I need a modern and edgy brochure to introduce my new business TORV Design, Commercial and Residential Building Designers.

We specialise in Building Design, Project Management and Design Consultation.

I would like the brochure to be anywhere between 2-4 pages, depending of amount of suitable content available.
Colours to be black and white with splashes of
bright colours (mostly incorporated in photos).

Main Content of brochure to be broken up into 3 (maybe 4) sections to include:

About Us
Services
Projects

Logo Text (DESIGN etc) can be changed to white if suits better with black background.

Would be nice to include sketches to give it that architectural feel.

Samples and wording will be uploaded shortly
Updates

I HAVE PROVIDED A COMPLETE UPDATE OF PROJECT REQUIREMENTS INCLUDING ALL NEW UPLOADED FILES.

PLEASE REFER TO THE BROCHURE LAYOUT PDF UPLOADEDĀ FOR FULL INFORMATION ON PROJECT INCLUDING BROCHURE LAYOUT.

IF YOU HAVE ANY QUESTIONS OR REQUIRE ANY FURTHER INFORMATION, PLEASE LET ME KNOW

I HAVE ADDED FURTHER DEVELOPED PDF DOCUMENTS OF BROCHURE.

IF YOU HAVE TROUBLE OPENING THESE DOCS IN ADOBE ILLUSTRATOR THRU ADOBE BRIDGE PLEASE LET ME KNOW & I WILL UPLOAD AI FILES.

CAN YOU PLEASE FINE TUNE GRAPHICS AND WORK ON BACKGROUND

Target Market(s)

Builders, Property Developers, Architects, Consultants, Professionals

Industry/Entity Type

Business

Requirements
Must have
• Very Professional Look
Black and White
Simple and easy to read layout
Either A4 (if only 2 pages) or
A3 double sided with centre fold (if 4 pages)
Touch up of photos (if possible) to make them stand out of the page.
Samples of recent projects with photos
Should not have
• Any comics or similar

```html
<!DOCTYPE html>
<html lang="en">
<head>
<meta charset="utf-8">
<title>TORV Design – Brochure Cover</title>
<link rel="stylesheet" href="https://fonts.googleapis.com/css2?family=Alegreya+Sans:wght@300;400;800&family=Alegreya+Sans+SC:wght@800&display=swap">
<style>
  :root {
    --ground: #d9d9db;
    --ink: #000000;
    --paper: #fbfbf8;
    --paper-edge: #b9b9b9;
    --accent: #ec3e9a;
    --reverse: #ffffff;
    --sketch-a: #141414;
    --sketch-b: #050505;
  }
  * { box-sizing: border-box; margin: 0; padding: 0; }
  html, body {
    width: 1200px;
    height: 872px;
    overflow: hidden;
    background: var(--ground);
  }
  .canvas {
    position: relative;
    width: 1200px;
    height: 872px;
  }
  .cover {
    position: absolute;
    left: 76px;
    top: 72px;
    width: 1041px;
    height: 734px;
    background: var(--ink);
    overflow: hidden;
  }
  .cover-art {
    position: absolute;
    left: 0;
    top: 0;
    width: 1041px;
    height: 734px;
  }
  .brand {
    position: absolute;
    left: 586px;
    top: 184px;
    width: 410px;
    font-family: "Alegreya Sans", sans-serif;
  }
  .brand-name {
    font-weight: 300;
    font-size: 178px;
    line-height: 1;
    letter-spacing: 0.06em;
    color: var(--accent);
    margin-left: -6px;
  }
  .brand-tagline {
    margin-top: 10px;
    font-weight: 800;
    font-size: 17.5px;
    letter-spacing: 0.01em;
    color: var(--ink);
    white-space: nowrap;
  }
  .brand-rule {
    margin-top: 14px;
    width: 398px;
    height: 2px;
    background: var(--accent);
  }
  .brand-quote {
    margin-top: 11px;
    width: 410px;
    font-weight: 400;
    font-size: 17px;
    line-height: 25px;
    color: var(--ink);
  }
  .contact {
    position: absolute;
    left: 24px;
    top: 694px;
    width: 1000px;
    display: flex;
    gap: 11px;
    align-items: baseline;
    font-family: "Alegreya Sans", sans-serif;
    font-weight: 800;
    font-size: 18px;
    color: var(--reverse);
    white-space: nowrap;
  }
  .contact .web {
    font-family: "Alegreya Sans SC", sans-serif;
    font-weight: 800;
    text-transform: lowercase;
  }
  .contact .divider { font-weight: 800; }
</style>
</head>
<body>
<main class="canvas">
  <section class="cover">
    <svg class="cover-art" viewBox="0 0 1041 734" aria-hidden="false">
      <defs>
        <linearGradient id="sketchTone" x1="0" y1="0" x2="1" y2="1">
          <stop offset="0" stop-color="var(--sketch-a)"/>
          <stop offset="1" stop-color="var(--sketch-b)"/>
        </linearGradient>
      </defs>
      <rect class="sketch-area" x="0" y="0" width="700" height="734" fill="url(#sketchTone)" role="img" aria-label="Faint architectural wireframe sketch of a multi-storey building"/>
      <polygon class="sheet sheet-back" points="502,166 500,196 477,203 575,605 1041,548 1041,8 904,29" fill="var(--paper)"/>
      <polygon class="sheet sheet-front" points="522,236 904,36 1041,31 1041,535 546,574" fill="var(--paper)" stroke="var(--paper-edge)" stroke-width="1"/>
    </svg>

    <div class="brand">
      <h1 class="brand-name">TORV</h1>
      <p class="brand-tagline">COMMERCIAL + RESIDENTIAL BUILDING DESIGNERS</p>
      <div class="brand-rule"></div>
      <blockquote class="brand-quote">"creative thinking may mean simply the realisation that there is no particular virtue in doing things the way they have always been done"</blockquote>
    </div>

    <footer class="contact">
      <span class="address">PO BOX 382&nbsp; ELLERVALE WA 6917</span>
      <span class="divider">I</span>
      <span class="web">mara@torvdesign.com.au</span>
      <span class="divider">I</span>
      <span class="phone">0491 570 156</span>
      <span class="divider">I</span>
      <span class="web">www.torvdesign.com.au</span>
    </footer>
  </section>
</main>
</body>
</html>
```